Buch-/E-Book-Cover für historischen Fantasy-Roman (Band 1 einer Reihe)
Sehr nett und professionell. Wir konnten einige kleinere Änderungen nach der Gewinnerkürung noch besprechen. Es ist alles zu meiner vollsten Zufriedenheit.
Zielgruppe
Ich habe eine Historische-Fantasyreihe geschrieben. Wobei der historische Aspekt vordergründlich ist. Zielgruppe sind junge Erwachsene (nicht mit dem Genre YA zu verwechseln) und Erwachsene.
Zeitlich spielt der Roman vor Christus. Anlehnen kann man sich am antiken Griechenland.
Aufgabenstellung
Das Konzept des Covers muss serientauglich sein. Ich möchte eine gewisse Kontinuität, einen Wiedererkennungswert haben, der sich über alle zukünftigen Cover ziehen kann.
Der Titel ist 'Staub und Salz', darunter Band 1. Ich bräuchte das Cover später auch auf Englisch.
Grundsätzlich stelle ich mir das Cover weder kitschig, noch ganz minimalistisch vor. Ich könnte mir geometrische Muster, angelehnt an antiken Mosaike vorstellen, und dass die Schrift an das griechische Alphabet angelehnt ist.
Eine Zeichnung (Szenerie? Landschaft?) wäre eventuell schön, oder irgendeine Form von Blickfang. Einfarbiger Hintergrund mit einem Bild in der Mitte wäre mir glaube ich zu wenig.
Angehängte Bilder dienen lediglich der Inspiration, Symbole oä müssen nicht verwendet werden.
Ich habe für diese Reihe 15 Jahre lang recherchiert und bin daher etwas heikel, wenn es um den historischen Part geht. Rüstungen, Pferdesättel oder Waffen, die es damals nicht gab, würde ich nicht akzeptieren. Genausowenig wie verglaste Fenster oder unrealistische Kleidung. (Orientierung am antiken Griechenland vor Christus kann schon mal nicht schief gehen).
Sollten Personen abgebildet werden, möchte ich kein Gesicht frontal, oder gut kenntlich sehen. Der Leser soll Freiraum haben, sich die Protagonisten selbst vorzustellen. Haut und Haare wären entsprechend der Region etwas dunkler als in Nord und Mitteleuropa.
Das einzige, das mir eingefallen ist, wäre folgendes Bild, und ich bin mir unsicher, ob es als Cover geeignet ist, aber es würde zumindest zum Titel passen:
Unwetter. Nacht. Ein Blitz schlägt in eine bereits brennende Platane. Eine sehr junge Frau - sie würde einen langen Chiton und darüber ein langes Himation tragen, das als Schleier über den Kopf gezogen ist - sieht die brennende Platane an.
Ich wiederhole mich: Ihr Vorschlag muss diese Szene nicht darstellen. Ich bin auch unsicher, ob fotorealistisch in meinem histori..

```html
<!DOCTYPE html>
<html lang="de">
<head>
<meta charset="utf-8">
<title>Staub und Salz – Band 1 – Umschlag</title>
<link rel="stylesheet" href="https://fonts.googleapis.com/css2?family=Federo&family=EB+Garamond:wght@600&display=swap">
<style>
  :root {
    --page: #ffffff;
    --brown-deep: #5a2818;
    --brown-mid: #86412a;
    --rust: #b0592f;
    --ember: #dd8440;
    --glow: #f4c48a;
    --mosaic: #9a5436;
    --mosaic-line: rgba(70, 30, 16, 0.35);
    --gold: #e6c264;
    --gold-light: #f6e0a0;
    --gold-dark: #7d5a1c;
    --spine-shade: rgba(60, 26, 14, 0.55);
  }
  * { margin: 0; padding: 0; box-sizing: border-box; }
  html, body { width: 1200px; height: 1200px; overflow: hidden; background: var(--page); }
  .canvas { position: relative; width: 1200px; height: 1200px; }

  .wrap { position: absolute; left: 101px; top: 239px; width: 1005px; height: 728px; overflow: hidden; }

  .backdrop {
    position: absolute; inset: 0;
    background:
      radial-gradient(ellipse 220px 260px at 820px 420px, rgba(240,160,90,0.55), transparent 70%),
      radial-gradient(ellipse 200px 160px at 130px 470px, rgba(224,138,60,0.40), transparent 70%),
      radial-gradient(ellipse 260px 160px at 880px 80px, rgba(224,138,60,0.35), transparent 70%),
      linear-gradient(165deg, var(--brown-deep) 0%, var(--brown-mid) 35%, var(--rust) 65%, var(--brown-mid) 100%);
  }

  /* mosaic medallions: placeholder areas in their main tones */
  .mosaic { position: absolute; border-radius: 50%; }
  .mosaic--front {
    left: 560px; top: 318px; width: 420px; height: 420px;
    background: radial-gradient(circle, transparent 0 30%, rgba(154,84,54,0.55) 31% 48%, var(--mosaic-line) 49% 50%, rgba(154,84,54,0.45) 51% 70%, transparent 71%);
  }
  .mosaic--back {
    left: 150px; top: -20px; width: 560px; height: 560px;
    background: radial-gradient(circle, transparent 0 40%, rgba(120,58,36,0.35) 41% 62%, var(--mosaic-line) 63% 64%, rgba(120,58,36,0.25) 65% 70%, transparent 71%);
  }
  .mosaic--band-top {
    left: 558px; top: 0; width: 447px; height: 30px;
    background: linear-gradient(180deg, rgba(120,58,36,0.35), rgba(120,58,36,0.1));
    border-radius: 0;
  }

  .spine-shade {
    position: absolute; top: 0; bottom: 0; left: 465px; width: 82px;
    background: linear-gradient(90deg, var(--spine-shade), rgba(60,26,14,0.12) 35%, rgba(60,26,14,0.12) 65%, var(--spine-shade));
  }

  .frame {
    position: absolute; border: 2px solid var(--gold);
    box-shadow: inset 0 0 0 1px rgba(125,90,28,0.6), 0 1px 2px rgba(0,0,0,0.45);
  }
  .frame--back  { left: 27px;  top: 25px; width: 419px; height: 678px; }
  .frame--spine { left: 471px; top: 25px; width: 66px;  height: 678px; }
  .frame--front { left: 556px; top: 30px; width: 424px; height: 678px; }

  .gold-type {
    position: absolute; line-height: 1; text-align: center; text-transform: uppercase;
    font-family: "Federo", serif; font-weight: 400; color: var(--gold);
    text-shadow: 0 -1px 0 var(--gold-light), 0 1px 0 var(--gold-dark), 0 3px 4px rgba(0,0,0,0.45);
  }
  .gold-type--caps { text-transform: none; font-variant: small-caps; }

  /* front cover */
  .front-title-main { left: 556px; width: 424px; top: 78px;  font-size: 107px; }
  .front-title-join { left: 556px; width: 424px; top: 190px; font-size: 36px; }
  .front-title-last { left: 556px; width: 424px; top: 236px; font-size: 107px; }
  .front-volume     { left: 556px; width: 424px; top: 378px; font-size: 48px; }
  .front-author     { left: 556px; width: 424px; top: 624px; font-size: 42px; letter-spacing: 1px; }
  .front-emblem {
    position: absolute; left: 690px; top: 455px; width: 150px; height: 150px; border-radius: 50%;
    background: radial-gradient(circle, rgba(246,200,140,0.9) 0%, rgba(221,132,64,0.7) 40%, rgba(176,89,47,0) 72%);
  }

  /* back cover */
  .back-title-main { left: 27px; width: 419px; top: 106px; font-size: 61px; }
  .back-title-join { left: 27px; width: 419px; top: 170px; font-size: 21px; }
  .back-title-last { left: 27px; width: 419px; top: 193px; font-size: 61px; }
  .back-blurb {
    position: absolute; left: 86px; top: 273px; width: 292px;
    font-family: "EB Garamond", serif; font-weight: 600; font-size: 13.6px; line-height: 14.6px;
    color: var(--glow); text-align: justify;
  }
  .back-volume { left: 27px; width: 419px; top: 464px; font-size: 31px; }
  .back-web {
    position: absolute; left: 86px; top: 620px;
    font-family: "EB Garamond", serif; font-weight: 600; font-size: 17px; color: var(--gold);
  }

  /* spine */
  .spine-text {
    position: absolute; left: 487px; width: 34px; white-space: nowrap;
    writing-mode: vertical-rl; transform: rotate(180deg);
    font-size: 32px; text-align: center;
  }
  .spine-title  { top: 84px; }
  .spine-author { top: 418px; }
</style>
</head>
<body>
<main class="canvas">
  <section class="wrap" aria-label="Buchumschlag Staub und Salz, Band 1">
    <div class="backdrop" role="img" aria-label="Gewitterhimmel in Rost- und Orangetönen mit Blitzen"></div>
    <div class="mosaic mosaic--back" role="img" aria-label="Großes griechisches Mäander-Mosaik, schwach im Hintergrund"></div>
    <div class="mosaic mosaic--band-top" role="img" aria-label="Mäanderband am oberen Rand"></div>
    <div class="mosaic mosaic--front" role="img" aria-label="Rundes griechisches Mosaik mit Mäander- und Spiralringen"></div>
    <div class="spine-shade"></div>

    <div class="frame frame--back"></div>
    <div class="frame frame--spine"></div>
    <div class="frame frame--front"></div>

    <!-- back cover -->
    <h2 class="gold-type back-title-main">Staub</h2>
    <p class="gold-type back-title-join">und</p>
    <h2 class="gold-type back-title-last">Salz</h2>
    <p class="back-blurb">Lorem ipsum dolor sit amet, consetetur sadipscing elitr, sed diam nonumy eirmod tempor invidunt ut labore et dolore magna aliquyam erat, sed diam voluptua. At vero eos et accusam et justo duo dolores et ea rebum. Stet clita kasd gubergren, no sea takimata sanctus est Lorem ipsum dolor sit amet. Lorem ipsum dolor sit amet, consetetur sadipscing elitr, sed diam nonumy eirmod tempor invidunt ut labore et dolore magna aliquyam erat, sed diam voluptua. At vero eos et accusam et justo duo dolores et ea rebum. Stet clita kasd gubergren, no sea takimata sanctus est Lorem ipsum dolor sit amet.</p>
    <p class="gold-type gold-type--caps back-volume">Band 1</p>
    <p class="back-web">www.loremipsum.xx</p>

    <!-- spine -->
    <p class="gold-type spine-text spine-title">Staub und Salz</p>
    <p class="gold-type gold-type--caps spine-text spine-author">Autoren Name</p>

    <!-- front cover -->
    <h1 class="gold-type front-title-main">Staub</h1>
    <p class="gold-type front-title-join">und</p>
    <p class="gold-type front-title-last">Salz</p>
    <p class="gold-type gold-type--caps front-volume">Band 1</p>
    <div class="front-emblem" role="img" aria-label="Vom Blitz getroffene, kahle Platane vor leuchtenden Gewitterwolken"></div>
    <p class="gold-type gold-type--caps front-author">Autoren Name</p>
  </section>
</main>
</body>
</html>
```